tax advisory service business cards
Professional
Loretta Fenwick
Tax Advisory Specialist
51924 HOLLISTER LANE SUITE C
ASHCOMBE, TN 70812
FISCAL9COUNSELDESK@QUILLMAIL.COM
FCD4FILE.COM

```html
<!DOCTYPE html>
<html lang="en">
<head>
<meta charset="utf-8">
<title>Fiscal Counsel Desk – Business Card</title>
<link href="https://fonts.googleapis.com/css2?family=Cinzel:wght@700&family=Open+Sans:wght@400;600&family=Tinos:ital@1&display=swap" rel="stylesheet">
<style>
  :root{
    --backdrop:#e6e7ea;
    --navy:#13224a;
    --navy-deep:#0c1736;
    --gold:#b8963e;
    --white:#ffffff;
    --silver:#e9eaed;
    --ink:#1b2440;
    --soft:#d7dbe6;
  }
  *{margin:0;padding:0;box-sizing:border-box}
  html,body{width:1200px;height:901px;overflow:hidden;background:var(--backdrop)}
  .stage{position:relative;width:1200px;height:901px}
  .card{position:absolute;left:290px;width:620px;height:354px;border-radius:22px;overflow:hidden;
        box-shadow:0 10px 28px rgba(10,20,50,.22)}
  /* back */
  .card-back{top:60px;background:linear-gradient(160deg,var(--navy) 0%,var(--navy-deep) 100%)}
  .back-mark{position:absolute;left:50%;top:120px;transform:translateX(-50%);
        display:flex;align-items:center;gap:14px}
  .back-mark .dot{width:70px;height:70px;border-radius:50%;background:var(--gold)}
  .back-mark .name{font-family:"Cinzel",serif;font-weight:700;font-size:22px;color:var(--white);white-space:nowrap}
  .back-web{position:absolute;left:0;right:0;top:236px;text-align:center;
        font-family:"Open Sans",sans-serif;font-size:13px;letter-spacing:3px;color:var(--soft)}
  /* front */
  .card-front{top:478px;background:var(--navy)}
  .front-top{position:absolute;left:0;top:0;width:100%;height:188px;
        background:linear-gradient(180deg,var(--white) 0%,var(--silver) 100%)}
  .brand{position:absolute;left:0;right:0;top:58px;display:flex;flex-direction:column;align-items:center}
  .brand-row{display:flex;align-items:center;gap:12px}
  .brand-row .dot{width:40px;height:40px;border-radius:50%;background:var(--navy)}
  .brand-name{font-family:"Cinzel",serif;font-weight:700;font-size:22px;color:var(--ink)}
  .tagline{margin-top:4px;font-family:"Tinos",serif;font-style:italic;font-size:11px;color:var(--ink)}
  .gold-rule{position:absolute;left:0;width:100%;background:var(--gold)}
  .rule-a{top:188px;height:4px}
  .rule-b{top:196px;height:1px;opacity:.7}
  .holder{position:absolute;left:48px;top:226px;font-family:"Open Sans",sans-serif;color:var(--white)}
  .holder-name{font-size:19px;font-weight:400}
  .holder-role{font-size:13px;color:var(--soft);margin-top:3px}
  .divider{position:absolute;left:300px;top:218px;width:1px;height:108px;background:var(--gold)}
  .contact{position:absolute;left:322px;top:220px;font-family:"Open Sans",sans-serif;font-size:12.5px;
        line-height:19px;color:var(--white);white-space:nowrap}
  .contact .line{display:flex;align-items:center;gap:8px}
  .contact .address{margin-bottom:8px}
  .contact svg{width:13px;height:13px;flex:none}
</style>
</head>
<body>
<div class="stage">
  <section class="card card-back">
    <div class="back-mark"><span class="dot"></span><span class="name">Fiscal Counsel Desk</span></div>
    <div class="back-web">fcd4file.com</div>
  </section>

  <section class="card card-front">
    <div class="front-top">
      <div class="brand">
        <div class="brand-row"><span class="dot"></span><span class="brand-name">Fiscal Counsel Desk, Inc.</span></div>
        <div class="tagline">Careful Filing and Clear Answers All Year</div>
      </div>
    </div>
    <div class="gold-rule rule-a"></div>
    <div class="gold-rule rule-b"></div>

    <div class="holder">
      <div class="holder-name">Loretta Fenwick</div>
      <div class="holder-role">Tax Advisory Specialist</div>
    </div>
    <div class="divider"></div>
    <div class="contact">
      <div class="address">51924 Hollister Lane Suite C<br>Ashcombe, TN 70812</div>
      <div class="line">
        <svg viewBox="0 0 16 16"><path fill="#b8963e" d="M3.5 1l2.5 3-1.5 2c1 2 3 4 5 5l2-1.5 3 2.5-1.5 2.5C7.5 15 1 8.5 1.5 2.5z"/></svg>
        555-201-0148
      </div>
      <div class="line">
        <svg viewBox="0 0 16 16"><rect x="1" y="3" width="14" height="10" rx="1" fill="#b8963e"/><path d="M1.5 3.5L8 9l6.5-5.5" stroke="#13224a" stroke-width="1.3" fill="none"/></svg>
        fiscal9counseldesk@quillmail.com
      </div>
      <div class="line">
        <svg viewBox="0 0 16 16"><circle cx="8" cy="8" r="6.5" fill="none" stroke="#b8963e" stroke-width="1.5"/><path d="M1.5 8h13M8 1.5c-3 3.5-3 9.5 0 13M8 1.5c3 3.5 3 9.5 0 13" stroke="#b8963e" stroke-width="1.2" fill="none"/></svg>
        www.fcd4file.com
      </div>
    </div>
  </section>
</div>
</body>
</html>
```